Small business updating business cards

We have already updated our logo via Pixel Forge and downloaded it (hopefully) for you to use. Now an updated set of business cards for Owen Brennan and Stuart Brennan are also needed... we are also hoping that a copy of our outdated business card designs have uploaded successfully as Microsoft Publisher files. Our Strength Through Unity motto has died a slow death so we are hoping to remove it (and other superfluous lingo if the graphic covers the idea) and instead opt for a fancy graphic (?) on the second side of the card that really reflects our desire to obtain product / haulage from Road Transport / Yard Operators and convert legs of their haulage to rail freight where profitable (bulk haulage / containterised etc). Can you help us look larger, bolder and more robust than we really are (two man show)?
Target Market(s)
Transport Industry
Industry/Entity Type
Business
Contact Information for Business Card
Card details for both O Brennan and S Brennan have been uploaded on the publisher files
Colors
Designer to choose colors to be used in the design.
Requirements
Must have
- Similar theme both sides of card
Should not have
- Black on one side white on the other

```html
<!DOCTYPE html>
<html lang="en">
<head>
<meta charset="utf-8">
<title>Railmark business cards</title>
<link href="https://fonts.googleapis.com/css2?family=Open+Sans:wght@400;600;700&family=Exo+2:wght@600;700&display=swap" rel="stylesheet">
<style>
  :root {
    --backdrop: #3a3230;
    --card: #1b1b1c;
    --logo-dim: #2e2e30;
    --gold: #d8a92a;
    --blue: #2a9cc4;
    --teal: #3aa7a4;
    --green: #7fae79;
    --yellow: #d7c24a;
    --text: #e9e9e9;
    --muted: #bdbdbd;
  }
  * { box-sizing: border-box; margin: 0; padding: 0; }
  html, body { width: 1200px; height: 715px; overflow: hidden; }
  body {
    background: var(--backdrop);
    font-family: "Open Sans", Arial, sans-serif;
    position: relative;
  }
  .card {
    position: absolute;
    top: 200px;
    width: 540px;
    height: 310px;
    background: var(--card);
    border-radius: 4px;
    box-shadow: 0 10px 24px rgba(0,0,0,.35);
    overflow: hidden;
  }
  .card--back { left: 40px; }
  .card--front { left: 620px; }

  /* reverse side */
  .back-logo {
    position: absolute;
    left: 0; right: 0; top: 84px;
    text-align: center;
    font-weight: 700;
    font-size: 64px;
    letter-spacing: 1px;
    color: var(--logo-dim);
  }
  .back-contact {
    position: absolute;
    left: 0; right: 0; bottom: 48px;
    text-align: center;
    color: var(--gold);
    font-size: 14px;
    line-height: 1.6;
  }

  /* front side */
  .name-block {
    position: absolute;
    left: 34px; top: 30px;
    padding-left: 16px;
    border-left: 6px solid var(--blue);
  }
  .name {
    font-family: "Exo 2", "Open Sans", sans-serif;
    font-weight: 600;
    font-size: 22px;
    color: var(--blue);
    letter-spacing: .5px;
  }
  .role { font-size: 11px; color: var(--muted); margin-top: 2px; }

  .brand {
    position: absolute;
    right: 36px; top: 118px;
    font-weight: 700;
    font-size: 42px;
    line-height: 1;
    color: var(--teal);
  }

  .contact-list {
    position: absolute;
    left: 34px; top: 140px;
    list-style: none;
    color: var(--text);
    font-size: 14px;
    line-height: 24px;
  }
  .contact-list li { display: flex; align-items: center; gap: 10px; }
  .contact-list svg { width: 12px; height: 12px; fill: var(--muted); flex: none; }

  .band {
    position: absolute;
    left: 0; right: 0; bottom: 0;
    height: 34px;
    background: linear-gradient(90deg, var(--blue) 0%, var(--teal) 30%, var(--green) 65%, var(--yellow) 100%);
    display: flex; align-items: center;
    padding-left: 34px;
    color: #fff;
    font-size: 10.5px;
    letter-spacing: .4px;
    text-transform: uppercase;
    white-space: nowrap;
  }
</style>
</head>
<body>

  <section class="card card--back" aria-label="Card reverse">
    <div class="back-logo">Railmark</div>
    <div class="back-contact">
      <p>www.railmark.com.au</p>
      <p>railmark@postbox.com &nbsp;|&nbsp; railmark@mailnest.com</p>
    </div>
  </section>

  <section class="card card--front" aria-label="Card front">
    <div class="name-block">
      <p class="name">Owen Brennan</p>
      <p class="role">Managing Director</p>
    </div>

    <p class="brand">Railmark</p>

    <ul class="contact-list">
      <li>
        <svg viewBox="0 0 12 12" aria-hidden="true"><path d="M2.5 0.5l2 2.5-1.2 1.3a7 7 0 0 0 4.4 4.4L9 7.5l2.5 2-1.3 2A10 10 0 0 1 0.5 1.8z"/></svg>
        0400 555 218
      </li>
      <li>
        <svg viewBox="0 0 12 12" aria-hidden="true"><path d="M0.5 2h11v8h-11z M1 2.5l5 4 5-4" stroke="#1b1b1c" stroke-width=".8"/></svg>
        brennano@railmark.com.au
      </li>
      <li>
        <svg viewBox="0 0 12 12" aria-hidden="true"><circle cx="6" cy="6" r="5.5"/><path d="M0.5 6h11M6 0.5v11" stroke="#1b1b1c" stroke-width=".8"/></svg>
        www.railmark.com.au
      </li>
      <li>14 Harlow Street Westbrook NSW 2290</li>
    </ul>

    <div class="band">Strategic Alliance Partners &nbsp;|&nbsp; Providing Logistical Freight Solutions</div>
  </section>

</body>
</html>
```